Crelvana Website

We need a website for our company. We have an off the shelf one now and it needs to be completely revamped. Crelvana provides design and manufacturing services mainly to medical device companies. We do precision machining with CNC milling machines. We envision our website having pictures of our clean environment, machining equipment and video of a device while is in the process of being cut. We take pride in our quality and craftsmanship. We like our logo, but the resolution may need to be improved, color can be changed. We like blue. We have a lot of high resolution pictures of the parts we have made and can provide video too.
Our current website is www.crelvanafab.example, some of the information can be taken from there. The business flyer attached has the most updated customer and equipment information. The Crelvana flyer has timeless information and example of pictures.

Font styles to use
Serif

Colors
33a6d7
0355a3

Requirements
Must have
• Contact Information
• About
• Equipment list
• Quality committment
• Pictures
Nice to have
• Place for Testimonials
• Video

```html
<!DOCTYPE html>
<html lang="en">
<head>
<meta charset="utf-8">
<title>Crelvana Engineering</title>
<link href="https://fonts.googleapis.com/css2?family=Open+Sans:wght@400;600;700&display=swap" rel="stylesheet">
<style>
:root{
  --blue:#0355a3;
  --sky:#33a6d7;
  --ink:#333;
  --muted:#666;
  --line:#9fd3ea;
  --dark:#111;
  --white:#fff;
}
*{box-sizing:border-box;margin:0;padding:0}
html,body{width:1200px;height:3922px;overflow:hidden}
body{font-family:"Open Sans",Arial,sans-serif;color:var(--ink);background:var(--white);position:relative}
.abs{position:absolute}
.btn{display:inline-block;background:var(--blue);color:var(--white);font-weight:600;font-size:15px;padding:6px 16px;border-radius:3px}
.section-title{font-size:32px;font-weight:600;color:var(--blue)}
.section-title span{color:var(--ink)}
p.body{font-size:13px;line-height:1.45;color:var(--muted);margin-bottom:12px}

/* header */
.header{top:0;left:0;width:1200px;height:118px}
.brand{left:90px;top:18px;display:flex;align-items:center;gap:10px}
.brand-mark{width:22px;height:22px;background:var(--blue);border-radius:50%}
.brand-name{font-size:26px;font-weight:600;color:var(--blue)}
.socials{right:80px;top:10px;display:flex;gap:8px}
.socials i{width:20px;height:20px;background:var(--blue);border-radius:3px;display:block}
.header-contact{right:80px;top:52px;text-align:right;font-size:14px;color:var(--blue);line-height:1.7}
.nav{top:118px;left:0;width:1200px;height:39px;background:var(--blue);display:flex;padding-left:110px}
.nav a{color:var(--white);font-size:15px;font-weight:600;text-decoration:none;padding:0 24px;line-height:39px}
.nav a.active{background:#3a72ad}

/* hero */
.hero{top:157px;left:0;width:1200px;height:504px;background:linear-gradient(120deg,#5a6b78,#a9b3ba 45%,#6c7680);text-align:center;color:var(--white)}
.hero h1{position:absolute;top:168px;width:100%;font-size:56px;font-weight:700;letter-spacing:2px}
.hero h2{position:absolute;top:236px;width:100%;font-size:28px;font-weight:600;letter-spacing:1px}
.hero .btn{position:absolute;top:314px;left:490px;width:220px;font-size:30px;padding:4px 0}

/* about */
.about-text{left:82px;top:700px;width:580px}
.about-text .section-title{margin-bottom:14px;border-bottom:2px solid #ccc;padding-bottom:8px;width:520px}
.about-photo{left:740px;top:753px;width:379px;height:280px;border:3px solid var(--blue);background:linear-gradient(#e9ecef 0 55%,#7a9a5a 55%)}

/* equipment */
.equip{top:1072px;left:0;width:1200px;height:457px;background:var(--blue)}
.equip h2{text-align:center;color:var(--white);font-size:32px;font-weight:600;margin-top:18px}
.equip-card{top:99px;width:220px}
.equip-photo{height:241px;background:linear-gradient(#8e9aa6,#56626d);position:relative}
.equip-photo span{position:absolute;bottom:6px;width:100%;text-align:center;color:var(--white);font-size:23px;font-weight:600}
.equip-card .ghost{display:block;margin:21px auto 0;width:128px;border:2px solid var(--white);color:var(--white);font-size:14px;text-align:center;padding:3px 0;border-radius:3px}

/* quality */
.quality-text{left:82px;top:1594px;width:560px}
.quality-text .section-title{margin-bottom:14px;border-bottom:2px solid #ccc;padding-bottom:8px;width:520px}
.video{left:654px;top:1605px;width:465px;height:311px;background:linear-gradient(135deg,#3d4650,#8a9098 50%,#2f363d)}
.video svg{position:absolute;left:202px;top:125px}

/* gallery */
.gallery-title{top:1996px;width:1200px;text-align:center}
.filters{left:82px;top:2083px;display:flex;gap:10px}
.filters span{font-size:13px;border:1px solid var(--blue);color:var(--blue);padding:1px 10px;border-radius:3px}
.filters span.on{background:var(--blue);color:var(--white)}
.tile{width:214px;height:177px;border-radius:10px}

/* testimonial */
.testimonial{top:2635px;left:0;width:1200px;height:340px;background:linear-gradient(#0b0b0b,#2a2a2a);color:var(--white);text-align:center}
.testimonial h3{margin-top:28px;font-size:26px;font-weight:600}
.testimonial h3 span{color:var(--sky)}
.avatar{left:530px;top:85px;width:102px;height:102px;border-radius:50%;background:#8d9298;border:3px solid var(--white)}
.arrow{top:125px;width:34px;height:26px;border:1px solid #777;display:flex;align-items:center;justify-content:center}
.quote-mark{left:225px;top:188px;font-size:90px;color:var(--sky);font-weight:700;line-height:1}
.testimonial p{position:absolute;left:315px;top:225px;width:580px;font-size:13px;line-height:1.6;color:#ddd}
.client{top:290px;width:1200px;font-size:13px;color:var(--sky)}

/* contact */
.contact-title{top:2994px;width:1200px;text-align:center}
.field{border:1px solid var(--line);height:41px;font-size:12px;color:#999;padding:10px}
.submit{left:196px;top:3330px;width:175px;height:34px;background:var(--sky);color:var(--white);font-weight:600;font-size:16px;text-align:center;line-height:34px}
.info{top:3435px;width:300px;text-align:center;font-size:13px;color:var(--muted);line-height:1.5}
.info svg{display:block;margin:0 auto 12px}
.map{top:3547px;left:0;width:1200px;height:333px;background:linear-gradient(#e3e5e8,#d5d8dc)}
.footer{top:3880px;left:0;width:1200px;height:42px;background:var(--dark);color:#ccc;font-size:13px;line-height:42px;padding-left:84px}
.footer .icons{position:absolute;right:70px;top:14px;display:flex;gap:14px}
.footer .icons i{width:12px;height:12px;background:#888;display:block}
</style>
</head>
<body>

<header class="abs header">
  <div class="abs brand"><i class="brand-mark"></i><span class="brand-name">Crelvana</span></div>
  <div class="abs socials"><i></i><i></i><i></i><i></i></div>
  <div class="abs header-contact">Call Us Now : 408 555 0192 &#9990;<br>E-mail : info@crelvanafab.example &#9993;</div>
</header>

<nav class="abs nav">
  <a class="active">Home</a><a>About</a><a>Equipment List</a><a>Quality Committment</a><a>Gallery</a><a>Testimonials</a><a>Contact Us</a>
</nav>

<section class="abs hero" role="img" aria-label="Machinists operating CNC equipment in a clean workshop">
  <h1>DESIGN PROTOTYPE PRODUCTION</h1>
  <h2>FOR THE MEDICAL DEVICE INDUSTRY</h2>
  <span class="btn">Know More</span>
</section>

<section class="abs about-text">
  <h2 class="section-title"><span>About</span> Crelvana</h2>
  <p class="body">Crelvana was founded in 2004 by Daniel Marsh with the purpose of providing high quality design and prototyping services to the medical device industry.</p>
  <p class="body">Daniel began his career in 1987 working as a machinist's apprentice at an injection molding company in Southern California. During his apprenticeship, Daniel acquired a foundation for the skills needed to produce tight tolerance molds and he attained hands on experience with injection molding. This early exposure to machining and injection molding would later provide a unique opportunity, as an Engineer, to streamline the development process by keeping the prototyping phase of the project in house.</p>
  <p class="body">Since graduating from Westbrook Polytechnic with a B.S. in Industrial Technology, Daniel has spent the last 15 years working for medical device start-ups developing hand held devices, miniature mechanisms and manufacturing fixturing for minimally invasive surgery. He has also consulted for medical companies on similar design and prototyping projects.</p>
  <span class="btn">Know More</span>
</section>
<div class="abs about-photo" role="img" aria-label="Crelvana office building entrance"></div>

<section class="abs equip">
  <h2>Equipment List</h2>
  <div class="abs equip-card" style="left:84px"><div class="equip-photo" role="img" aria-label="CNC milling machines in clean shop"><span>Milling</span></div><span class="ghost">All Products</span></div>
  <div class="abs equip-card" style="left:350px"><div class="equip-photo" role="img" aria-label="Lathe turning a part with coolant lines"><span>Turning</span></div><span class="ghost">All Products</span></div>
  <div class="abs equip-card" style="left:617px"><div class="equip-photo" role="img" aria-label="Surface grinding machine"><span>Surface Grinding</span></div><span class="ghost">All Products</span></div>
  <div class="abs equip-card" style="left:884px"><div class="equip-photo" role="img" aria-label="Injection molding press"><span>Injection Molding</span></div><span class="ghost">All Products</span></div>
</section>

<section class="abs quality-text">
  <h2 class="section-title">Quality <span>Committment</span></h2>
  <p class="body">Lorem ipsum dolor sit amet, no eum gubergren sadipscing. Ea his velit denique persecuti. Possit nemore te eum. Eu graecis conceptam has, posse theophrastus in mei, in eam dolor eruditi accommodare.</p>
  <p class="body">Graeci expetenda te qui, an quot laudem nec, his cu soluta graecis. Vim enim constituam ea. Ad noster audiam his, vel aperiri albucius in, eu everti dolorem forensibus quo. In mei consul putent facilisis, dolor clita at mei. Case etiam intellegat ius ad, et quo elit luctus omittam.</p>
  <p class="body">Lorem ipsum dolor sit amet, no eum gubergren sadipscing. Ea his velit denique persecuti. Possit nemore te eum. Eu graecis conceptam has, posse theophrastus in mei, in eam dolor eruditi accommodare.</p>
  <span class="btn">Know More</span>
</section>
<div class="abs video" role="img" aria-label="Video of a device part being cut on a lathe">
  <svg width="60" height="60" viewBox="0 0 60 60"><circle cx="30" cy="30" r="29" fill="#fff" opacity=".9"/><path d="M24 18 L42 30 L24 42 Z" fill="#0355a3"/></svg>
</div>

<h2 class="abs section-title gallery-title">Gallery</h2>
<div class="abs filters"><span class="on">All</span><span>Milling</span><span>Turning</span><span>Grinding</span></div>
<div class="abs tile" style="left:136px;top:2159px;background:linear-gradient(135deg,#4b535b,#9aa0a6)" role="img" aria-label="Machined part in a fixture"></div>
<div class="abs tile" style="left:374px;top:2159px;background:linear-gradient(135deg,#c9b79a,#e6dccb)" role="img" aria-label="Molded plastic component"></div>
<div class="abs tile" style="left:612px;top:2159px;background:linear-gradient(135deg,#3e4a55,#b6bcc2)" role="img" aria-label="Part held in lathe chuck"></div>
<div class="abs tile" style="left:850px;top:2159px;background:linear-gradient(135deg,#d8d2c8,#b7ae9e)" role="img" aria-label="Miniature mechanism beside a coin"></div>
<div class="abs tile" style="left:136px;top:2368px;background:linear-gradient(135deg,#b9b9b9,#e6e6e6)" role="img" aria-label="Clear plastic handheld device"></div>
<div class="abs tile" style="left:374px;top:2368px;background:linear-gradient(135deg,#2e2e2e,#a9a39a)" role="img" aria-label="Assembled device housing"></div>
<div class="abs tile" style="left:612px;top:2368px;background:linear-gradient(135deg,#a8a8a8,#d4d4d4)" role="img" aria-label="Small precision parts on a surface"></div>
<div class="abs tile" style="left:850px;top:2368px;background:linear-gradient(135deg,#bfae8c,#e2d5b8)" role="img" aria-label="Batch of molded plastic parts"></div>

<section class="abs testimonial">
  <h3>HAPPY <span>CLIENT</span></h3>
  <div class="abs arrow" style="left:450px"><svg width="12" height="10"><path d="M11 5H1M5 1L1 5L5 9" stroke="#aaa" fill="none"/></svg></div>
  <div class="abs avatar" role="img" aria-label="Client portrait"></div>
  <div class="abs arrow" style="left:660px"><svg width="12" height="10"><path d="M1 5H11M7 1L11 5L7 9" stroke="#aaa" fill="none"/></svg></div>
  <div class="abs quote-mark">&#8220;</div>
  <p>Lorem Ipsum is simply dummy text of the printing and typesetting. Lorem Ipsum is simply dummy text of the printing and typesetting. Lorem Ipsum is simply dummy text of the printing and typesetting. Lorem Ipsum is simply dummy text of the printing and typesetting.</p>
  <div class="abs client">Alan Reeve, CEO</div>
</section>

<h2 class="abs section-title contact-title">Contact Us</h2>
<div class="abs field" style="left:196px;top:3072px;width:251px">Your Name</div>
<div class="abs field" style="left:476px;top:3072px;width:251px">Company</div>
<div class="abs field" style="left:753px;top:3072px;width:251px">Your E-Mail</div>
<div class="abs field" style="left:196px;top:3137px;width:808px;height:157px">Your Comments</div>
<div class="abs submit">Submit</div>

<div class="abs info" style="left:186px">
  <svg width="22" height="30" viewBox="0 0 22 30"><path d="M11 0C5 0 0 5 0 11c0 8 11 19 11 19s11-11 11-19C22 5 17 0 11 0z" fill="#33a6d7"/><circle cx="11" cy="11" r="4" fill="#fff"/></svg>
  Crelvana Engineering, LLC<br>1420 Harlow Ave Bldg. 6<br>Sunnyvale, CA 94089
</div>
<div class="abs info" style="left:470px">
  <svg width="34" height="24" viewBox="0 0 34 24"><rect width="34" height="24" rx="2" fill="#33a6d7"/><path d="M1 1L17 14L33 1" stroke="#fff" stroke-width="2" fill="none"/></svg>
  info@crelvanafab.example
</div>
<div class="abs info" style="left:754px">
  <svg width="26" height="26" viewBox="0 0 26 26"><path d="M6 1l5 5-3 3c2 4 5 7 9 9l3-3 5 5-4 4C11 23 3 15 2 5z" fill="#33a6d7"/></svg>
  408-555-0192
</div>

<div class="abs map" role="img" aria-label="Street map showing the Crelvana location"></div>

<footer class="abs footer">Copyright &copy; 2016 Crelvana Engineering. All Right Reserved
  <div class="icons"><i></i><i></i><i></i><i></i><i></i><i></i></div>
</footer>

</body>
</html>
```